Domain Parking page and Listing page

1)
In need a design of a domain parking page, mainly with the same features as KOV.example as can be seen here: https://pickturnip.example/

2)
I need a design of a website with all domains listed. There's no company logo/name yet so it should be in plain font, for example "lotsbrim.example" (this is just an example), similar as:
https://kov.example/search?&terms=park&results=50&order_by=relevance

Delivery after approval in HTML/CSS. Should be responsive. Ideally use a framework like Bootstrap

Target Market(s)

Domain buyers, business owners

Industry/Entity Type

Business to business, Marketing, domains

Coding

Coded - Design and coding required

Number of Pages Required

2 page

Font styles to use
Sans Serif

Requirements
Must have
• Responsive design, worldly design.

```html
<!DOCTYPE html>
<html lang="en">
<head>
<meta charset="utf-8">
<title>claimyourmarknow.example is for sale</title>
<link href="https://fonts.googleapis.com/css2?family=Poppins:wght@300;400;500;600;700&display=swap" rel="stylesheet">
<style>
:root{
  --green-deep:#1f7f5a;
  --green-hero:#3f8a6d;
  --green-light:#9ef2a8;
  --green-btn:#4fa35c;
  --green-tick:#43a35a;
  --mint-bg:#eef7f5;
  --banner-a:#6ea68c;
  --banner-b:#72c3a0;
  --ink:#1d2a27;
  --muted:#6e7a77;
  --white:#ffffff;
  --line:#e2e6e5;
}
*{box-sizing:border-box;margin:0;padding:0}
html,body{width:914px;height:1200px;overflow:hidden}
body{font-family:'Poppins',sans-serif;background:var(--mint-bg);position:relative;color:var(--ink)}
.abs{position:absolute}
.hero-bg{left:0;top:0;width:914px;height:300px}
.globe{left:470px;top:40px;width:420px;height:250px;border-radius:50% 50% 0 0;background:radial-gradient(circle at 55% 45%,#5aa488 0%,#2f7a5e 60%,rgba(47,122,94,0) 100%);opacity:.8}
.brand{display:flex;align-items:center;gap:6px;color:var(--white);font-size:12px;font-weight:500}
.brand-mark{width:14px;height:14px;border-radius:3px;background:var(--green-light)}
.topbar{left:72px;top:13px}
.rating{right:74px;top:19px;font-size:8.3px;color:#d8ece4;display:flex;align-items:center;gap:4px}
.rating b{color:var(--white);font-weight:600}
.rating .rate-brand{font-size:10px;color:var(--white);font-weight:500;margin-left:3px}
.rating .sq{width:9px;height:9px;background:var(--white)}
.top-rule{left:74px;top:43px;width:767px;height:1px;background:rgba(255,255,255,.35)}
.headline{left:72px;top:86px;color:var(--white)}
.headline .lead{font-size:23px;font-weight:400;line-height:36px}
.headline .domain{font-size:27px;font-weight:700;color:var(--green-light);line-height:36px}
.offer-card{left:210px;top:220px;width:495px;height:215px;background:var(--white);border-radius:4px;box-shadow:0 8px 24px rgba(20,60,45,.12);text-align:center}
.offer-card h2{font-size:18px;font-weight:600;color:#4a4f4e;margin-top:17px}
.offer-card .vat{font-size:10px;color:var(--muted);margin-top:5px}
.offer-card .vat a{color:var(--green-deep);font-weight:500}
.offer-row{position:absolute;left:26px;top:77px;display:flex;gap:10px}
.offer-input{width:219px;height:37px;border:1px solid #dfe3e2;border-radius:3px;font-size:10px;color:#333;text-align:left;padding:11px 16px}
.offer-btn{width:216px;height:37px;background:var(--green-btn);border-radius:3px;color:var(--white);font-size:10px;font-weight:600;display:flex;align-items:center;justify-content:center;gap:6px}
.perks{position:absolute;left:26px;top:138px;width:445px;display:flex;justify-content:space-between;font-size:10px;color:#333}
.perks span{display:flex;align-items:center;gap:4px}
.perks em{font-style:normal;color:var(--green-tick)}
.card-rule{position:absolute;left:25px;top:168px;width:450px;height:1px;background:var(--line)}
.pay{position:absolute;left:113px;top:182px;display:flex;gap:7px}
.pay i{display:block;width:27px;height:16px;border-radius:2px}
.features{left:90px;top:493px;width:740px;display:flex;justify-content:space-between}
.feature{width:200px;text-align:center}
.feature .art{width:40px;height:40px;margin:0 auto 10px;border-radius:6px;background:linear-gradient(135deg,#c8efe4,#8fd8c2)}
.feature h3{font-size:14px;font-weight:500;line-height:19px;color:var(--ink)}
.feature p{font-size:10px;line-height:15.3px;color:#333;margin-top:11px}
.feature p b{font-weight:600}
.foot-bg{left:0;top:820px;width:914px;height:380px}
.banner{left:86px;top:725px;width:742px;height:172px;border-radius:14px;background:linear-gradient(180deg,var(--banner-a),var(--banner-b));text-align:center;color:var(--white);overflow:hidden}
.banner .swirl{position:absolute;border-radius:50%;background:rgba(255,255,255,.12)}
.banner h2{font-size:20px;font-weight:600;margin-top:30px}
.banner p{font-size:10px;line-height:15.2px;color:#eef8f3;width:440px;margin:12px auto 0}
.banner p b{font-weight:600;color:var(--white)}
.banner .how{display:inline-flex;gap:6px;align-items:center;font-size:10px;font-weight:600;margin-top:15px}
.footer-brand{left:93px;top:944px}
.footer-brand .brand{font-size:12.5px}
.footer-brand .short-rule{width:42px;height:1px;background:rgba(255,255,255,.4);margin:12px 0 10px}
.footer-brand p{font-size:8.8px;line-height:13.5px;color:#d9efe6;width:200px}
.contact{font-size:8.5px;color:#e4f3ed;display:flex;align-items:center;gap:7px;margin-top:9px}
.contact a{color:#e4f3ed}
.col{top:950px;color:var(--white)}
.col h4{font-size:9.5px;font-weight:600;letter-spacing:.2px;margin-bottom:10px}
.col li{list-style:none;font-size:10px;color:#e0f1ea;line-height:17.8px}
.social{display:flex;gap:5px}
.social i{display:block;width:19px;height:19px;border-radius:3px;background:rgba(255,255,255,.35)}
.lang{margin-top:16px;font-size:10px;font-weight:600;display:inline-flex;gap:6px;align-items:center;border-bottom:1px solid rgba(255,255,255,.5);padding:0 2px 2px}
.foot-rule{left:96px;top:1081px;width:732px;height:1px;background:rgba(255,255,255,.25)}
.copy{left:0;top:1094px;width:914px;text-align:center;font-size:10px;color:#e4f3ed}
.disclaimer{left:93px;top:1131px;width:740px;color:var(--white)}
.disclaimer h5{font-size:10px;font-weight:600}
.disclaimer p{font-size:8.7px;line-height:13.5px;color:#dff0e9;margin-top:6px}
</style>
</head>
<body>

<svg class="abs hero-bg" viewBox="0 0 914 300" aria-hidden="true">
  <defs><linearGradient id="heroGrad" x1="0" y1="0" x2="1" y2="1">
    <stop offset="0" stop-color="#4a9175"/><stop offset="1" stop-color="#2e7c5c"/></linearGradient></defs>
  <path d="M0 0H914V257Q700 290 457 290Q220 290 0 257Z" fill="url(#heroGrad)"/>
</svg>
<div class="abs globe" role="img" aria-label="Dotted globe illustration with orbiting lines"></div>

<div class="abs topbar brand"><span class="brand-mark"></span>lotsbrim.example</div>
<div class="abs rating">Our customers say <b>Excellent</b> <b>5.0</b> out of 5 stars based on 52,352 reviews <span class="rate-brand">Ratewell</span><span class="sq"></span></div>
<div class="abs top-rule"></div>

<div class="abs headline">
  <div class="lead">Congratulation!</div>
  <div class="domain">claimyourmarknow.example</div>
  <div class="lead">is for sale</div>
</div>

<section class="abs offer-card">
  <h2>Make an offer</h2>
  <p class="vat">Excluding 21.0%VAT <a href="#">Learn more</a></p>
  <div class="offer-row">
    <div class="offer-input">My Offer in USD</div>
    <div class="offer-btn">Go to next step
      <svg width="11" height="9" viewBox="0 0 11 9"><path d="M0 4.5H10M6.5 1L10 4.5 6.5 8" stroke="#fff" stroke-width="1.2" fill="none"/></svg></div>
  </div>
  <div class="perks">
    <span><svg width="10" height="10" viewBox="0 0 10 10"><circle cx="5" cy="5" r="4.4" stroke="#43a35a" fill="none"/><path d="M3 5.2L4.5 6.6 7.2 3.7" stroke="#43a35a" fill="none"/></svg><em>Free</em> Ownership transfer</span>
    <span><svg width="10" height="10" viewBox="0 0 10 10"><circle cx="5" cy="5" r="4.4" stroke="#43a35a" fill="none"/><path d="M3 5.2L4.5 6.6 7.2 3.7" stroke="#43a35a" fill="none"/></svg><em>Free</em> Transaction support</span>
    <span><svg width="10" height="10" viewBox="0 0 10 10"><circle cx="5" cy="5" r="4.4" stroke="#43a35a" fill="none"/><path d="M3 5.2L4.5 6.6 7.2 3.7" stroke="#43a35a" fill="none"/></svg>Secure payments</span>
  </div>
  <div class="card-rule"></div>
  <div class="pay" aria-label="Accepted payment methods">
    <i style="background:#252b6b"></i><i style="background:#1a1a1a"></i><i style="background:#18307a"></i><i style="background:#2d7fd3"></i><i style="background:#f09a2b"></i><i style="background:#e6e6e6"></i><i style="background:#000"></i><i style="background:#1d3f8f"></i>
  </div>
</section>

<section class="abs features">
  <div class="feature">
    <div class="art" role="img" aria-label="Line icon of a checklist with a raised hand and coin"></div>
    <h3>Declare Your<br>Interest</h3>
    <p>Submit your bid for<br><b>ClaimYourMarkNow.example</b> using the provided input box.</p>
  </div>
  <div class="feature">
    <div class="art" role="img" aria-label="Line icon of documents exchanged with arrows"></div>
    <h3>Safe Transaction<br>Process</h3>
    <p>Once your offer is accepted, our team will guide you through a secure payment process, putting your mind at ease.</p>
  </div>
  <div class="feature">
    <div class="art" role="img" aria-label="Line icon of a browser window and server"></div>
    <h3>Seamless Domain<br>Transition</h3>
    <p>Our experts will oversee the domain transfer process, providing unwavering support at every stage.</p>
  </div>
</section>

<svg class="abs foot-bg" viewBox="0 0 914 380" aria-hidden="true">
  <path d="M0 26Q457 -60 914 26V380H0Z" fill="#1f8058"/>
</svg>

<section class="abs banner">
  <div class="swirl" role="img" aria-label="Faint line-art flourish" style="left:-20px;top:0;width:110px;height:120px"></div>
  <div class="swirl" role="img" aria-label="Faint line-art flourish" style="right:-10px;top:30px;width:130px;height:150px"></div>
  <h2>Embrace the Possibilities Now!</h2>
  <p>Entrepreneurs, innovators, and creators, the domain you've been waiting for is within reach. <b>ClaimYourMarkNow.example</b> offers the key to online prominence and brand excellence. Don't let this opportunity pass you by.</p>
  <a class="how">How it works
    <svg width="11" height="9" viewBox="0 0 11 9"><path d="M0 4.5H10M6.5 1L10 4.5 6.5 8" stroke="#fff" stroke-width="1.2" fill="none"/></svg></a>
</section>

<div class="abs footer-brand">
  <div class="brand"><span class="brand-mark"></span>lotsbrim.example</div>
  <div class="short-rule"></div>
  <p>Have questions or need assistance? Reach out to our dedicated support team at</p>
  <div class="contact" style="margin-top:12px"><svg width="10" height="8" viewBox="0 0 10 8"><rect x=".5" y=".5" width="9" height="7" stroke="#fff" fill="none"/><path d="M.5 .5L5 4.5 9.5 .5" stroke="#fff" fill="none"/></svg><a href="#" style="text-decoration:underline">help@lotsbrim.example</a></div>
  <div class="contact"><svg width="9" height="9" viewBox="0 0 9 9"><path d="M1 1.5L2.8 1 4 3 3 4Q4 6 5.2 6.2L6.2 5 8.2 6.3 7.6 8Q2 7.5 1 1.5Z" fill="#fff"/></svg>1-800-555-0147.</div>
</div>

<div class="abs col" style="left:359px">
  <h4>HELP CENTER</h4>
  <ul><li>Help centre</li><li>FAQ</li><li>Quick Start Guide</li><li>Tutorials</li><li>Associate Blog</li></ul>
</div>
<div class="abs col" style="left:516px">
  <h4>MY ACCOUNT</h4>
  <ul><li>Manage Accounts</li><li>How to Withdraw</li><li>Account Varification</li><li>Safety &amp; Security</li><li>Membership Level</li></ul>
</div>
<div class="abs col" style="left:682px">
  <h4>FOLLOW US</h4>
  <div class="social"><i></i><i></i><i></i><i></i></div>
  <div class="lang">English <svg width="6" height="4" viewBox="0 0 6 4"><path d="M0 0H6L3 3.5Z" fill="#fff"/></svg></div>
</div>

<div class="abs foot-rule"></div>
<div class="abs copy">Copyright © 2019.All Rights Reserved By lotsbrim.example</div>
<div class="abs disclaimer">
  <h5>Disclaimer</h5>
  <p>The information provided on this page is for informational purposes only and does not constitute legal or financial advice. All domain sales are subject to applicable terms and conditions. Prices and availability are subject to change without notice.</p>
</div>

</body>
</html>
```